Need A Modern Website Design For ADSL2+ Provider

AIM: To sell affordable combined ADSL2+ Unlimited & phone line rentals to residential customers.

TYPE: This project is for DESIGN only (no code)

Source Files: I need all source files, fonts, images to be provided in ZIP format.

Logo: Existing (attached)

-Corporate Colours-
Black & Red (Same as Logo)
Others colours are fine as long as it looks corporate and modern.

-Pages-
Need another page to display our pricing plan

(1)Homepage Design
(2)Page to display our plans (needs to be in tables)
Example: http://lnkbrev.example/QwTr8k

-Pricing Plan-
(1) $59.95 / Month (Metro / City Areas)
(2) $79.95 / Month (Outside City Areas / Rural Areas)
Detailed Pricing plans is in PDF attached
Updates

Target Market(s)

Both male & female, Young & Old

Industry/Entity Type

Residential

Requirements
Must have
• + Graphic banner on the home page that shows our ADSL2+ combo plan for ADSL2+ Unlimited & Phone Line Rental for only $59.95

+ A box to allow customers to login to their account (username & password + login button)

+ Clearly display contact number
+ Button to sign up
+ Button to check service availability something like https://checkin.pelwara.example/wizard/

+ Button for Live Chat
+ Navigation menu
+ Social media icons Facebook, Google +, Twitter
+ Minimal text on homepage
+ Corporate & Friendly
Nice to have
• + Effective use of icons with corporate colours
+ Effective use of stockphotos
(use of people in photos would be nice)

+ Effective use of graphics to navigate people through the site and inform customers of specials,etc.
Should not have
• + Cluttered
+ Don’t want long scrolling homepage
+ Don’t want too much text on homepage 500 words is the estimate max.

```html
<!DOCTYPE html>
<html lang="en">
<head>
<meta charset="utf-8">
<title>Corvane – ADSL2+ Unlimited</title>
<link rel="stylesheet" href="https://fonts.googleapis.com/css2?family=Marcellus&family=Arimo:wght@400;700&family=Roboto+Condensed:wght@400;700&display=swap">
<style>
:root{
  --red:#c8201f;
  --red-dark:#9e1414;
  --black:#1f1c1d;
  --ink:#111;
  --grey-bg:#e6e6e6;
  --grey-line:#e3e3e3;
  --muted:#555;
  --yellow:#ffe600;
  --white:#fff;
}
*{box-sizing:border-box;margin:0;padding:0}
html,body{width:1116px;height:1200px;overflow:hidden;background:var(--white)}
body{position:relative;font-family:"Arimo",Arial,sans-serif;color:var(--ink)}
.abs{position:absolute}
.serif{font-family:"Marcellus",Georgia,serif}

/* header */
.brand{left:129px;top:43px;display:flex;align-items:center;gap:10px}
.brand-dot{width:46px;height:46px;border-radius:50%;background:var(--black)}
.brand-name{font-family:"Marcellus",Georgia,serif;font-size:31px;letter-spacing:1px;color:var(--black)}
.main-nav{left:386px;top:63px;display:flex;font-size:13px}
.main-nav a{color:var(--black);text-decoration:none;padding:0 12px;border-left:1px solid #999;line-height:14px}
.main-nav a:first-child{border-left:none;padding-left:0;color:var(--red)}
.call{left:691px;top:59px;display:flex;align-items:center;gap:7px;font-size:17px}
.call svg{width:22px;height:22px}
.social{left:906px;top:58px;display:flex;gap:4px}
.social span{width:24px;height:24px;background:#444;border-radius:2px}
.social span:first-child{background:var(--red)}
.signup-tab{left:895px;top:107px;width:92px;height:26px;background:var(--black);color:var(--white);font-size:13px;display:flex;align-items:center;justify-content:flex-end;padding-right:10px;gap:8px;clip-path:polygon(8px 0,100% 0,100% 100%,0 100%)}
.signup-tab svg{width:20px;height:14px}

/* banner */
.banner-rule{left:129px;top:128px;width:858px;height:6px;background:var(--black)}
.banner{left:129px;top:134px;width:858px;height:326px;background:radial-gradient(ellipse at 55% 45%,#d22c27,#b81b1a 70%,#a41615);border-bottom:9px solid var(--red-dark)}
.banner-band{left:472px;top:208px;width:515px;height:49px;background:linear-gradient(90deg,rgba(30,26,27,0),var(--black) 18%)}
.promo-text{z-index:2}
.promo-title{left:472px;width:390px;top:213px;text-align:center;color:var(--white);font-size:31px;letter-spacing:1px}
.promo-sub{left:472px;width:390px;top:259px;text-align:center;color:var(--white);font-size:25px}
.promo-for{left:520px;width:240px;top:299px;display:flex;align-items:center;gap:10px;color:var(--black);font-size:13px;letter-spacing:8px}
.promo-for i{flex:1;height:1px;background:var(--black)}
.promo-price{left:520px;width:240px;top:316px;text-align:center;font-family:"Arimo",Arial,sans-serif;font-weight:700;font-size:58px;color:var(--yellow);text-shadow:0 2px 3px rgba(0,0,0,.35)}
.photo-person{left:134px;top:113px;width:300px;height:347px;background:linear-gradient(180deg,#d8b39c 0%,#3b3d44 40%,#25272d 100%);border-radius:40% 40% 0 0/18% 18% 0 0}
.photo-modems-left{left:322px;top:166px;width:150px;height:190px;background:linear-gradient(160deg,#6b6b6b,#2d2d2d);border-radius:6px}
.photo-router-left{left:413px;top:343px;width:150px;height:86px;background:linear-gradient(160deg,#8a8a8a,#333);border-radius:6px}
.photo-modem-right{left:890px;top:172px;width:66px;height:118px;background:linear-gradient(160deg,#7a7a7a,#333);border-radius:6px}
.photo-router-right{left:760px;top:285px;width:222px;height:92px;background:linear-gradient(160deg,#7a7a7a,#2e2e2e);border-radius:6px}

/* availability strip */
.chat-panel{left:129px;top:465px;width:231px;height:105px;background:var(--red)}
.chat-art{left:116px;top:473px;width:118px;height:103px;background:radial-gradient(circle at 40% 40%,#e3f1ff,#8fbde8 70%,#5f97cf);border-radius:50% 50% 50% 50%/55% 55% 45% 45%}
.chat-small{left:241px;top:494px;color:var(--white);font-size:12px}
.chat-big{left:241px;top:505px;color:var(--white);font-family:"Roboto Condensed",Arial,sans-serif;font-weight:700;font-size:30px;letter-spacing:-.5px}
.check-panel{left:360px;top:465px;width:627px;height:105px;background:var(--black);color:var(--white)}
.check-title{left:378px;top:472px;font-size:18px;color:var(--white)}
.check-input{left:378px;top:500px;width:500px;height:26px;background:var(--white);border-radius:3px;display:flex;align-items:center;gap:10px;padding-left:8px;font-size:13px;color:#444}
.check-input svg{width:14px;height:14px}
.btn-browse{left:884px;top:500px;width:80px;height:26px;background:#e0312f;border-radius:3px;color:var(--white);font-size:15px;display:flex;align-items:center;justify-content:center}
.check-note{left:378px;top:533px;width:320px;font-size:10px;line-height:13px;color:#bbb}
.dont-call{left:791px;top:536px;display:flex;align-items:center;gap:5px;font-size:12px;color:#ccc}
.dont-call i{width:9px;height:9px;background:#ddd}

/* login */
.login{left:129px;top:615px;width:229px;height:179px;background:var(--grey-bg);border-top:4px solid var(--red);padding:20px 16px}
.login h2{font-weight:400;font-size:18px;color:var(--red);margin-bottom:12px}
.field{height:25px;background:var(--white);font-size:12px;color:#333;padding:6px 7px;margin-bottom:8px}
.login-foot{display:flex;justify-content:space-between;align-items:center;margin-top:4px}
.login-links{font-size:11px;line-height:14px}
.btn-login{width:77px;height:24px;background:var(--red);border-radius:3px;color:var(--white);font-size:13px;display:flex;align-items:center;justify-content:center}

/* welcome */
.welcome-title{left:381px;top:610px;font-size:22px;color:var(--red);font-weight:400}
.welcome-lead{left:383px;top:644px;width:604px;font-size:14.5px;line-height:17px}
.welcome-body{left:383px;top:692px;width:445px;font-size:12px;line-height:17px}
.photo-team{left:841px;top:697px;width:146px;height:95px;background:linear-gradient(135deg,#c8924f,#6a3a17 70%,#3a1d0c)}

/* features */
.rule{left:129px;width:858px;height:3px;background:var(--grey-line)}
.feature{width:250px;text-align:center}
.feature-icon{width:42px;height:42px;border-radius:50%;background:var(--grey-bg);margin:0 auto;display:flex;align-items:center;justify-content:center}
.feature-icon svg{width:20px;height:20px}
.feature h3{font-family:"Marcellus",Georgia,serif;font-weight:400;font-size:19px;color:var(--red);margin-top:16px}
.feature p{font-size:12px;line-height:17px;margin:20px auto 0;width:232px}
.feature p em{font-style:normal;color:var(--red)}

/* footer */
.footer-nav{left:0;width:1116px;top:1126px;display:flex;justify-content:center;font-size:12px}
.footer-nav a{color:var(--ink);text-decoration:none}
.footer-nav a:first-child{color:var(--red)}
.footer-nav b{margin:0 10px;font-weight:700}
.copyright{left:0;width:1116px;top:1155px;text-align:center;font-size:11.5px}
</style>
</head>
<body>

<header>
  <div class="abs brand"><span class="brand-dot"></span><span class="brand-name">CORVANE</span></div>
  <nav class="abs main-nav"><a href="#">Home</a><a href="#">About Us</a><a href="#">Our Plans</a><a href="#">Contact Us</a></nav>
  <div class="abs call">
    <svg viewBox="0 0 22 22"><circle cx="11" cy="11" r="11" fill="#9a9a9a"/><path d="M7 6c1-1 2 0 2.5 1.2l.5 1.3c.2.6-.3 1-.7 1.3.5 1.3 1.4 2.2 2.7 2.7.3-.4.7-.9 1.3-.7l1.3.5c1.2.5 2.2 1.5 1.2 2.5-1.5 1.5-4 .8-6.2-1.4S5.5 7.5 7 6z" fill="#fff"/></svg>
    Call Us: 000-000-0000
  </div>
  <div class="abs social" aria-label="Social media links"><span></span><span></span><span></span></div>
  <div class="abs signup-tab">
    <svg viewBox="0 0 20 14"><circle cx="6" cy="4" r="3" fill="#f0c040"/><circle cx="14" cy="4" r="3" fill="#7fb0e0"/><path d="M0 14c0-4 3-6 6-6s6 2 6 6z" fill="#f0c040"/><path d="M8 14c0-4 3-6 6-6s6 2 6 6z" fill="#7fb0e0"/></svg>
    Sign Up
  </div>
</header>

<section aria-label="Promotion">
  <div class="abs banner-rule"></div>
  <div class="abs banner"></div>
  <div class="abs banner-band"></div>
  <div class="abs photo-modems-left" role="img" aria-label="Two ADSL modems standing upright"></div>
  <div class="abs photo-router-left" role="img" aria-label="Wireless router with antenna"></div>
  <div class="abs photo-modem-right" role="img" aria-label="Upright ADSL modem"></div>
  <div class="abs photo-router-right" role="img" aria-label="Wireless router with network ports"></div>
  <div class="abs photo-person" role="img" aria-label="Smiling businessman in a suit with arms crossed"></div>
  <div class="abs serif promo-text promo-title">ADSL2+ UNLIMITED</div>
  <div class="abs serif promo-text promo-sub">&amp; Phone Line Rental</div>
  <div class="abs serif promo-text promo-for"><i></i>FOR ONLY<i></i></div>
  <div class="abs promo-text promo-price">$59.95</div>
</section>

<section aria-label="Service availability">
  <div class="abs chat-panel"></div>
  <div class="abs chat-art" role="img" aria-label="Glossy speech bubbles"></div>
  <div class="abs chat-small">Click Here to Start</div>
  <div class="abs chat-big">Live Chat</div>
  <div class="abs check-panel"></div>
  <div class="abs check-title">Check service availability</div>
  <div class="abs check-input">
    <svg viewBox="0 0 14 14"><path d="M3 1c1-.6 1.7.2 2 1l.5 1.2c.2.6-.2 1-.6 1.3.5 1.3 1.3 2.1 2.6 2.6.3-.4.7-.8 1.3-.6L10 7c.8.3 1.6 1 1 2-1 1.6-3.6.8-5.6-1.2S1.5 2 3 1z" fill="#999"/></svg>
    Enter your phone number
  </div>
  <div class="abs btn-browse">Browse</div>
  <p class="abs check-note">By entering a number you agree that we may contact you to discuss the availability of services in your area.</p>
  <div class="abs dont-call"><i></i>Don't Call me</div>
</section>

<section class="abs login" aria-label="User login">
  <h2>User Login</h2>
  <div class="field">username</div>
  <div class="field">password</div>
  <div class="login-foot">
    <div class="login-links">• forgot password?<br>• forgot username?</div>
    <div class="btn-login">Login</div>
  </div>
</section>

<section aria-label="Welcome">
  <h1 class="abs serif welcome-title">Welcome to Corvane</h1>
  <p class="abs welcome-lead">Nam quis ligula a nibh fermentum venenatis vitae nec neque. Etiam non felis Quisque feugiat, lectus non feugiat consectetur,</p>
  <p class="abs welcome-body">Sed lacinia vulputate dolor, nec congue nunc accumsan at. Praesent leo magna, imperdiet et mollis sed, hendrerit id nunc. Vestibulum et dolor enim. Cum sociis natoque penatibus et magnis dis parturient montes, nascetur ridiculus mus. Aenean accumsan varius nulla id euismod. Morbi blandit, odio dignissim laoreet bibendum, nibh sapien condimentum lectus, in semper eros magna vel neque. Aliquam quis mauris accumsan.</p>
  <div class="abs photo-team" role="img" aria-label="Business team meeting around a conference phone"></div>
</section>

<div class="abs rule" style="top:845px"></div>

<section aria-label="Highlights">
  <div class="abs feature" style="left:150px;top:886px">
    <div class="feature-icon"><svg viewBox="0 0 20 20"><rect x="6" y="3" width="12" height="10" fill="#444"/><rect x="4" y="5" width="12" height="10" fill="#666" stroke="#e6e6e6"/><rect x="2" y="7" width="12" height="10" fill="#333" stroke="#e6e6e6"/></svg></div>
    <h3>Corvane Plans</h3>
    <p>Sed lacinia vulputate dolor, nec congue nunc accumsan at. Praesent leo magna, imperdiet et mollis sed,</p>
  </div>
  <div class="abs feature" style="left:428px;top:886px">
    <div class="feature-icon"><svg viewBox="0 0 20 20"><path d="M2 3h16v11H8l-4 4v-4H2z" fill="#333"/><circle cx="6.5" cy="8.5" r="1" fill="#fff"/><circle cx="10" cy="8.5" r="1" fill="#fff"/><circle cx="13.5" cy="8.5" r="1" fill="#fff"/></svg></div>
    <h3>Client Speak</h3>
    <p>“ Sed lacinia vulputate dolor, nec congue nunc accumsan at. Praesent leo magna, imperdiet et mollis sed, “ <em>- Laoreet sit</em></p>
  </div>
  <div class="abs feature" style="left:714px;top:886px">
    <div class="feature-icon"><svg viewBox="0 0 20 20"><rect x="3" y="2" width="5" height="16" rx="1" fill="#333"/><rect x="9" y="5" width="8" height="13" rx="1" fill="#555"/><rect x="10.5" y="7" width="5" height="3" fill="#ddd"/><g fill="#ddd"><rect x="10.5" y="11.5" width="1.5" height="1.5"/><rect x="13.5" y="11.5" width="1.5" height="1.5"/><rect x="10.5" y="14.5" width="1.5" height="1.5"/><rect x="13.5" y="14.5" width="1.5" height="1.5"/></g></svg></div>
    <h3>Contact Corvane</h3>
    <p>Aenean iaculis risus a erat dictum venenatis. Pellentesque convallis fringilla est, at laoreet orci ullamcorper</p>
  </div>
</section>

<div class="abs rule" style="top:1078px"></div>

<footer>
  <nav class="abs footer-nav">
    <a href="#">Home</a><b>•</b><a href="#">About Us</a><b>•</b><a href="#">Our Plans</a><b>•</b><a href="#">Contact Us</a><b>•</b><a href="#">Login</a><b>•</b><a href="#">Sign Up</a><b>•</b><a href="#">Terms</a><b>•</b><a href="#">Privacy</a>
  </nav>
  <p class="abs copyright">© Corvane 2013. All Rights Reserved.</p>
</footer>

</body>
</html>
```